TallowBrookLending.com

We are setting up a new company to make small business loans over the internet. We have a logo. Customers will apply on line, so the online application must allow customers to upload files.

We need a complete design and also a some who can build the online application and website for us (CODING). When applicants fill out fields, at various points they may be able to move to the next questions or receive a notice that their application is not eligible for funding.

Sample sites are: MerrowVantage.com/us, BrinlowPact.com, Quorvex.com, Tamsley.com, PelwarTrust.com, norbellyard.com, vontrila.com.

We think WordPress makes the most sense but we are open to suggestions.

Note, we will request that the winning designer build the site for us including the online application. We will negotiate this separately, I presume, before we pick the final winner.

Target Market(s)

Small businesses in the United States.

Industry/Entity Type

Small Business

Requirements
Must have
• Online application - fields and ability to upload basic files.

https://filevault.example-drive.test/redir?resid=A41D2F9E7C3B0E8!58027&authkey=!KWpRtZ482mXoDvQ&ithint=file,.pdf

```html
<!DOCTYPE html>
<html lang="en">
<head>
<meta charset="utf-8">
<title>TallowBrookLending.com – Small Business Loans</title>
<link href="https://fonts.googleapis.com/css2?family=Open+Sans:wght@400;600;700;800&display=swap" rel="stylesheet">
<style>
:root{
  --orange:#f26522;
  --orange-dark:#d9531a;
  --blue:#2b7ba8;
  --blue-light:#3a93c2;
  --navy:#1b5574;
  --navy-deep:#164a66;
  --ink:#444;
  --muted:#777;
  --grey-bg:#eeeeee;
  --line:#d6d6d6;
  --white:#fff;
}
*{box-sizing:border-box;margin:0;padding:0}
html,body{width:735px;height:1200px;overflow:hidden;background:var(--white)}
body{position:relative;font-family:"Open Sans",Arial,sans-serif;color:var(--ink);font-size:7px;line-height:1.45}
.abs{position:absolute}

/* header */
.site-header{position:absolute;left:0;top:0;width:735px;height:48px;background:var(--white)}
.brand{position:absolute;left:137px;top:12px;display:flex;align-items:center;gap:5px}
.brand-dot{width:20px;height:20px;border-radius:50%;background:var(--orange)}
.brand-name{font-size:16px;font-weight:700;color:var(--navy);letter-spacing:-.2px}
.header-actions{position:absolute;left:470px;top:18px;display:flex;gap:4px}
.btn-sm{height:13px;padding:0 6px;font-size:6px;font-weight:700;color:#fff;display:flex;align-items:center;text-transform:uppercase}
.btn-login{background:var(--orange)}
.btn-signup{background:var(--navy)}
.phone{border:1px solid var(--line);border-radius:3px;color:var(--ink);font-weight:600;margin-left:6px;text-transform:none}

/* nav */
.main-nav{position:absolute;left:0;top:48px;width:735px;height:23px;background:var(--blue);border-top:3px solid var(--blue-light)}
.main-nav ul{list-style:none;display:flex;position:absolute;left:137px;top:0;height:20px}
.main-nav li{height:20px;padding:0 12px;display:flex;align-items:center;color:#fff;font-size:6.5px;font-weight:600;text-transform:uppercase;gap:4px}
.main-nav li.active{background:var(--navy-deep)}
.nav-ico{width:5px;height:5px;border-radius:1px;background:rgba(255,255,255,.8)}

/* hero */
.hero{position:absolute;left:0;top:71px;width:735px;height:289px;border-bottom:3px solid var(--blue)}
.hero-photo{position:absolute;inset:0;background:linear-gradient(90deg,#d8c39e 0%,#c7b28e 20%,#9aa07a 38%,#e9dfcb 58%,#f4efe6 75%,#d9cdb9 100%)}
.hero-copy{position:absolute;left:447px;top:16px;width:147px;text-align:center;text-transform:uppercase}
.hero-copy .kicker{font-size:10px;color:var(--orange);font-weight:400}
.hero-copy .big{font-size:21px;font-weight:800;color:var(--orange);line-height:1}
.hero-copy .sub{font-size:10px;color:var(--orange);border-bottom:1px solid var(--orange);padding-bottom:4px}
.hero-copy .cta{font-size:7px;font-weight:700;color:var(--navy);margin-top:6px;line-height:1.35}
.apply-card{position:absolute;left:447px;top:106px;width:147px;height:174px;background:var(--white);box-shadow:0 1px 4px rgba(0,0,0,.25)}
.apply-head{height:21px;margin:5px 0 0;background:var(--orange);color:#fff;font-size:7px;font-weight:700;text-transform:uppercase;display:flex;align-items:center;justify-content:center}
.apply-form{padding:7px 6px 0}
.row{display:flex;gap:6px;margin-bottom:6px}
.field{flex:1;height:15px;border:1px solid var(--line);font-size:5px;color:#999;padding:0 4px;display:flex;align-items:center;justify-content:space-between}
.field .caret{width:0;height:0;border-left:2.5px solid transparent;border-right:2.5px solid transparent;border-top:3px solid #555}
.row.gap{margin-top:10px}
.privacy{font-size:5px;text-align:center;color:var(--ink);margin-top:2px}
.privacy b{color:var(--orange)}
.btn-next{display:block;margin:6px auto 0;width:90px;height:17px;border-radius:9px;background:var(--navy);color:#fff;font-size:5.5px;font-weight:700;text-transform:uppercase;display:flex;align-items:center;justify-content:center}

/* section titles */
.section-title{position:absolute;height:22px;background:var(--white);border:1px solid #e3e3e3;box-shadow:0 2px 3px rgba(0,0,0,.1);font-size:8px;font-weight:700;color:var(--navy);text-transform:uppercase;display:flex;align-items:center;justify-content:center}

/* how it works */
.how{position:absolute;left:0;top:363px;width:735px;height:190px;background:var(--grey-bg)}
.steps-line{position:absolute;left:187px;top:99px;width:360px;height:2px;background:#cfcfcf}
.step{position:absolute;top:56px;width:110px;margin-left:-55px;text-align:center}
.step svg{display:block;margin:0 auto}
.step-title{margin-top:7px;font-size:9px;font-weight:700;color:var(--navy);text-transform:uppercase}
.step-sub{font-size:6.5px;color:var(--ink)}

/* why */
.why{position:absolute;left:0;top:553px;width:735px;height:207px;background:var(--white)}
.why-intro{position:absolute;left:190px;top:62px;width:355px;text-align:center;font-size:6.5px}
.feature{position:absolute;top:90px;width:147px}
.feature-head{display:flex;align-items:center;gap:8px;height:40px}
.feature-icon{width:40px;height:40px;border-radius:50%;background:var(--navy);flex:none;display:flex;align-items:center;justify-content:center}
.feature-title{font-size:8.5px;font-weight:700;color:var(--blue);text-transform:uppercase;line-height:1.25;border-bottom:1px solid var(--line);padding-bottom:3px}
.feature-title em{font-style:normal;color:var(--orange)}
.feature p{margin-top:12px;font-size:5.6px;color:var(--muted);line-height:1.6}
.feature p em{font-style:normal;color:var(--orange)}

/* testimonials */
.testimonials{position:absolute;left:0;top:760px;width:735px;height:154px;background:var(--grey-bg)}
.quote{position:absolute;top:59px;width:220px}
.avatar{position:absolute;left:0;top:0;width:59px;height:49px;border:2px solid #fff;box-shadow:0 0 2px rgba(0,0,0,.3)}
.quote-mark{position:absolute;left:63px;top:-4px;font-size:22px;font-weight:800;color:#bbb;line-height:1}
.quote-text{position:absolute;left:78px;top:0;width:142px;font-size:5.6px;color:var(--ink);line-height:1.55}
.quote-author{position:absolute;left:63px;top:42px;font-size:5.6px;font-weight:700;color:var(--navy);white-space:nowrap}
.quote-author span{color:var(--orange);font-weight:600}
.btn-pill{position:absolute;left:320px;top:122px;width:91px;height:18px;border-radius:9px;background:var(--navy);color:#fff;font-size:5.8px;font-weight:700;text-transform:uppercase;display:flex;align-items:center;justify-content:center}

/* featured */
.featured{position:absolute;left:0;top:914px;width:735px;height:140px;background:var(--white)}
.press-slider{position:absolute;left:137px;top:60px;width:460px;height:56px;border:1px solid var(--line);border-radius:4px;background:#f4f4f4}
.slide-arrow{position:absolute;top:12px;width:15px;height:30px;display:flex;align-items:center;justify-content:center}
.slide-prev{left:0;background:#bdbdbd}
.slide-next{right:0;background:var(--orange)}
.press-item{position:absolute;top:8px;width:97px;height:38px;background:var(--white);border:1px solid #e4e4e4;border-radius:3px;display:flex;align-items:center;justify-content:center;text-align:center;font-size:9px;font-weight:700;color:#222;line-height:1.1}

/* footer */
.site-footer{position:absolute;left:0;top:1054px;width:735px;height:146px;background:linear-gradient(180deg,#1d5f82,#174e6c);color:#d7e6ef}
.foot-col{position:absolute;top:14px}
.foot-col h4{font-size:6.2px;font-weight:600;color:#fff;text-transform:uppercase;margin-bottom:5px}
.foot-col li{list-style:none;font-size:5.6px;line-height:1.5;color:#b8d0de}
.foot-col li::before{content:"• ";color:#b8d0de}
.foot-brand{position:absolute;left:137px;top:78px;display:flex;align-items:center;gap:4px}
.foot-brand .brand-dot{width:14px;height:14px;background:#5c86a0}
.foot-brand .brand-name{font-size:12px;color:#7ea3ba}
.badge{position:absolute;top:76px;background:rgba(255,255,255,.55)}
.badge.round{width:26px;height:26px;border-radius:50%}
.badge.sq{width:36px;height:20px;border-radius:2px;top:79px}
.badge-label{position:absolute;top:79px;font-size:5px;font-weight:700;color:#fff;text-transform:uppercase;line-height:1.25}
.foot-text{position:absolute;left:137px;top:107px;width:460px;font-size:5px;color:#8fb2c6}
.copyright{position:absolute;left:137px;top:128px;font-size:5px;color:#8fb2c6}
</style>
</head>
<body>

<header class="site-header">
  <div class="brand"><span class="brand-dot"></span><span class="brand-name">TallowBrookLending.com</span></div>
  <div class="header-actions">
    <span class="btn-sm btn-login">Log in</span>
    <span class="btn-sm btn-signup">Sign up</span>
    <span class="btn-sm phone">555-018-2947</span>
  </div>
</header>

<nav class="main-nav">
  <ul>
    <li class="active"><span class="nav-ico"></span>Home</li>
    <li><span class="nav-ico"></span>About us</li>
    <li><span class="nav-ico"></span>Products</li>
    <li><span class="nav-ico"></span>Calculator</li>
    <li><span class="nav-ico"></span>Blog</li>
    <li><span class="nav-ico"></span>Contact us</li>
  </ul>
</nav>

<section class="hero">
  <div class="hero-photo" role="img" aria-label="Photo of a smiling small business owner in a green cardigan standing in her shop"></div>
  <div class="hero-copy">
    <div class="kicker">We create</div>
    <div class="big">Business</div>
    <div class="sub">Success stories</div>
    <div class="cta">Fill the form below<br>to apply for loan</div>
  </div>
  <div class="apply-card">
    <div class="apply-head">Apply for Tallow Brook Loan</div>
    <div class="apply-form">
      <div class="row"><div class="field">Name...</div><div class="field">Phone No...</div></div>
      <div class="row gap"><div class="field">Email Id...</div><div class="field">Monthly Income <i class="caret"></i></div></div>
      <div class="row"><div class="field">Type of Loan <i class="caret"></i></div><div class="field">Duration <i class="caret"></i></div></div>
      <div class="row"><div class="field">How much Do you want to borrow? <i class="caret"></i></div></div>
      <div class="privacy">Privacy &amp; Security Protected <b>More Info</b></div>
      <span class="btn-next">Proceed to next step</span>
    </div>
  </div>
</section>

<section class="how">
  <div class="section-title" style="left:317px;top:17px;width:101px">How it work</div>
  <div class="steps-line"></div>

  <div class="step" style="left:187px">
    <svg width="88" height="88" viewBox="0 0 88 88">
      <circle cx="44" cy="44" r="38" fill="#fff" stroke="#cfcfcf" stroke-width="9"/>
      <path d="M44 6 A38 38 0 0 1 82 44" fill="none" stroke="#f26522" stroke-width="9"/>
      <circle cx="40" cy="40" r="10" fill="none" stroke="#1b5574" stroke-width="3.5"/>
      <line x1="47" y1="47" x2="57" y2="57" stroke="#1b5574" stroke-width="5" stroke-linecap="round"/>
    </svg>
    <div class="step-title">Eligibility</div><div class="step-sub">Find your Eligibility</div>
  </div>

  <div class="step" style="left:307px">
    <svg width="88" height="88" viewBox="0 0 88 88">
      <circle cx="44" cy="44" r="38" fill="#fff" stroke="#cfcfcf" stroke-width="9"/>
      <path d="M44 6 A38 38 0 0 1 82 44 A38 38 0 0 1 44 82" fill="none" stroke="#f26522" stroke-width="9"/>
      <rect x="28" y="30" width="32" height="22" rx="2" fill="none" stroke="#1b5574" stroke-width="3.5"/>
      <rect x="38" y="54" width="12" height="4" fill="#1b5574"/>
      <circle cx="44" cy="41" r="5" fill="#1b5574"/>
    </svg>
    <div class="step-title">Online Application</div><div class="step-sub">Complete the Online Application</div>
  </div>

  <div class="step" style="left:427px">
    <svg width="88" height="88" viewBox="0 0 88 88">
      <circle cx="44" cy="44" r="38" fill="#fff" stroke="#cfcfcf" stroke-width="9"/>
      <path d="M44 6 A38 38 0 1 1 6 44" fill="none" stroke="#f26522" stroke-width="9"/>
      <rect x="30" y="32" width="24" height="24" rx="2" fill="none" stroke="#1b5574" stroke-width="3.5"/>
      <path d="M40 48 L56 30 L60 34 L44 52 L38 53 Z" fill="#1b5574"/>
    </svg>
    <div class="step-title">E-Sign Contract</div><div class="step-sub">E-Sign the Contract</div>
  </div>

  <div class="step" style="left:547px">
    <svg width="88" height="88" viewBox="0 0 88 88">
      <circle cx="44" cy="44" r="38" fill="#fff" stroke="#f26522" stroke-width="9"/>
      <rect x="30" y="34" width="30" height="18" fill="#fff" stroke="#1b5574" stroke-width="3"/>
      <rect x="26" y="38" width="30" height="18" fill="#fff" stroke="#1b5574" stroke-width="3"/>
      <circle cx="41" cy="47" r="4" fill="#1b5574"/>
    </svg>
    <div class="step-title">Amount</div><div class="step-sub">Get the Desire Amount</div>
  </div>
</section>

<section class="why">
  <div class="section-title" style="left:307px;top:21px;width:120px">Why TallowBrookLending</div>
  <p class="why-intro">All the Lorem Ipsum generators on the Internet tend to repeat predefined chunks as necessary, making this the first true generator on the Internet. It uses a dictionary of over 200 Latin words.</p>

  <div class="feature" style="left:137px">
    <div class="feature-head">
      <span class="feature-icon"><svg width="20" height="20" viewBox="0 0 20 20"><circle cx="10" cy="11" r="7" fill="none" stroke="#fff" stroke-width="2"/><path d="M10 7v4l3 2" stroke="#fff" stroke-width="1.6" fill="none"/></svg></span>
      <div class="feature-title">A fast, simple<br><em>loan process</em></div>
    </div>
    <p>All the Lorem Ipsum generators on the Internet tend to repeat predefined chunks as necessary, making this the first true generator on the Internet. It uses a dictionary of over 200 Latin words, <em>combined with a handful</em> of model sentence structures, to generate Lorem Ipsum.</p>
  </div>

  <div class="feature" style="left:293px">
    <div class="feature-head">
      <span class="feature-icon"><svg width="20" height="20" viewBox="0 0 20 20"><circle cx="10" cy="8" r="5" fill="none" stroke="#fff" stroke-width="2"/><path d="M7 12 L5 18 L10 16 L15 18 L13 12" fill="#fff"/></svg></span>
      <div class="feature-title">A company you can<br><em>trust</em></div>
    </div>
    <p>All the Lorem Ipsum generators on the Internet tend to repeat predefined <em>chunks as necessary, making this the first true generator on the Internet.</em> It uses a dictionary of over 200 Latin words, combined with a handful of model sentence structures, to generate Lorem Ipsum.</p>
  </div>

  <div class="feature" style="left:450px">
    <div class="feature-head">
      <span class="feature-icon"><svg width="20" height="20" viewBox="0 0 20 20"><rect x="3" y="7" width="14" height="10" rx="1.5" fill="#fff"/><rect x="7" y="4" width="6" height="4" fill="none" stroke="#fff" stroke-width="1.6"/></svg></span>
      <div class="feature-title">100% focused on<br><em>small business</em></div>
    </div>
    <p>All the Lorem Ipsum generators on the Internet tend to repeat predefined chunks as necessary, making this the first true <em>generator on the Internet</em>. It uses a dictionary of over 200 Latin words, combined with a handful of model sentence structures, to generate Lorem Ipsum.</p>
  </div>
</section>

<section class="testimonials">
  <div class="section-title" style="left:299px;top:18px;width:136px">What people are saying</div>

  <div class="quote" style="left:137px">
    <div class="avatar" role="img" aria-label="Portrait photo of a restaurant owner" style="background:linear-gradient(135deg,#d9b48a,#a8c6d8)"></div>
    <div class="quote-mark">“</div>
    <p class="quote-text">All the Lorem Ipsum generators on the Internet tend to repeat predefined chunks as necessary, making this the first true generator on the Internet. It uses a dictionary of over 200 Latin words.</p>
    <div class="quote-author">Marco Delavy | <span>RESTAURANT OWNER</span></div>
  </div>

  <div class="quote" style="left:377px">
    <div class="avatar" role="img" aria-label="Portrait photo of a florist" style="background:linear-gradient(135deg,#c98a5a,#e5d2c0)"></div>
    <div class="quote-mark">“</div>
    <p class="quote-text">All the Lorem Ipsum generators on the Internet tend to repeat predefined chunks as necessary, making this the first true generator on the Internet. It uses a dictionary of over 200 Latin words.</p>
    <div class="quote-author">Nadia Forsel | <span>FLORIST</span></div>
  </div>

  <span class="btn-pill">View all testimonials</span>
</section>

<section class="featured">
  <div class="section-title" style="left:333px;top:18px;width:85px">As featured in</div>
  <div class="press-slider">
    <span class="slide-arrow slide-prev"><svg width="6" height="9" viewBox="0 0 6 9"><path d="M5 0.5 L1 4.5 L5 8.5" fill="none" stroke="#fff" stroke-width="1.6"/></svg></span>
    <div class="press-item" style="left:18px">The Harlow Ledger</div>
    <div class="press-item" style="left:125px">Corvane Street Daily</div>
    <div class="press-item" style="left:232px">ByteMarrow</div>
    <div class="press-item" style="left:339px">Westrand Weekly</div>
    <span class="slide-arrow slide-next"><svg width="6" height="9" viewBox="0 0 6 9"><path d="M1 0.5 L5 4.5 L1 8.5" fill="none" stroke="#fff" stroke-width="1.6"/></svg></span>
  </div>
</section>

<footer class="site-footer">
  <div class="foot-col" style="left:137px"><h4>Loan apply</h4><ul><li>Apply Now</li><li>Manage Your Account</li><li>Example Loans</li></ul></div>
  <div class="foot-col" style="left:237px"><h4>How's &amp; Why's</h4><ul><li>Why Choose Us?</li><li>How it Work</li><li>News and Views</li></ul></div>
  <div class="foot-col" style="left:324px"><h4>Legal</h4><ul><li>Agreements</li><li>Website Terms</li><li>Policies</li></ul></div>
  <div class="foot-col" style="left:404px"><h4>More information</h4><ul><li>Affiliates</li><li>Media</li><li>Articles</li></ul></div>
  <div class="foot-col" style="left:503px"><h4>More information</h4><ul><li>FAQs</li><li>Site Map</li><li>Articles</li></ul></div>

  <div class="foot-brand"><span class="brand-dot"></span><span class="brand-name">TallowBrookLending.com</span></div>

  <span class="badge round" style="left:406px"></span>
  <span class="badge sq" style="left:456px"></span>
  <span class="badge sq" style="left:520px;width:12px;height:16px;top:81px"></span>
  <span class="badge-label" style="left:536px">Privacy &amp; Security<br>Protected</span>

  <p class="foot-text">All the Lorem Ipsum generators on the Internet tend to repeat predefined chunks as necessary, making this the first true generator on the Internet. It uses a dictionary of over 200 Latin words, combined with a handful of model sentence structures.</p>
  <p class="copyright">© Copyright 2014. TallowBrookLending.com. All Rights Reserved | Terms of Use | Disclaimer</p>
</footer>

</body>
</html>
```